Redesign (8 documents) attached with brand guidelines - very quick/easy job!

We have 8 flyers/documents that we need put into the style of our new brand (see attached). So this is a simple rebrand exercise - complete with our brand guidelines (see attached)

I would need the designer to sign an NDA prior to taking this piece of work as I will be sharing newly branded documents with you prior to market release.

If these are done well we would as the same designer to work on a z-card designed brochure/POS

Brief:

- These are documents that customers would need to complete in order to book a particular service
- If you use images (ideally from Pixmora, so we don’t have to pay for them!)
- Icon ideas enclosed
-All the content on the brochures is required: but if you think it would 'flow better' in a different order that is fine.

Customers interested in receiving a particular service

Work

• Brandon (see brand guide)

• A4
• New logo ideas
• Anything out of brand guidleines

```html
<!DOCTYPE html>
<html lang="en">
<head>
<meta charset="utf-8">
<title>Verdavia – Health Objectives</title>
<link rel="stylesheet" href="https://fonts.googleapis.com/css2?family=Nunito+Sans:wght@400;600;700;800&display=swap">
<style>
  :root {
    --teal: #1799bc;
    --teal-dark: #127f9c;
    --yellow: #f2e600;
    --frame: #a9a9a9;
    --row-bg: #e6e6e6;
    --label: #6b6b6b;
    --field: #555555;
    --paper: #ffffff;
  }
  * { box-sizing: border-box; margin: 0; padding: 0; }
  html, body { width: 848px; height: 1200px; overflow: hidden; background: var(--paper); }
  body { font-family: "Nunito Sans", Arial, sans-serif; }

  .sheet { position: relative; width: 848px; height: 1200px; overflow: hidden; background: var(--paper); }

  .backdrop-texture {
    position: absolute; left: 0; top: 160px; width: 520px; height: 1000px;
    background: radial-gradient(ellipse at 20% 30%, #eeeeee 0%, rgba(238,238,238,0.5) 40%, rgba(255,255,255,0) 70%);
  }

  .header-band { position: absolute; left: 0; top: 0; width: 600px; height: 200px; }

  .brand {
    position: absolute; left: 58px; top: 72px;
    font-weight: 800; font-size: 46px; letter-spacing: 1px;
    color: var(--yellow);
  }

  .doc-title {
    position: absolute; right: 69px; top: 172px;
    font-weight: 700; font-size: 26px; color: var(--teal);
  }

  .field {
    position: absolute; display: flex; align-items: baseline;
    font-size: 13px; font-weight: 700; color: var(--field);
  }
  .field .dots { flex: 1; border-bottom: 1.5px dotted #777; margin-left: 4px; transform: translateY(-3px); }
  .field--nutritionist { left: 424px; top: 242px; width: 355px; }
  .field--store { left: 424px; top: 290px; width: 355px; }
  .field--date { left: 424px; top: 336px; width: 355px; }
  .field--client { left: 71px; top: 336px; width: 330px; }

  .objectives {
    position: absolute; left: 68px; top: 369px; width: 715px; height: 778px;
    border: 3px solid var(--frame); border-radius: 14px;
    background: var(--row-bg); overflow: hidden;
  }
  .reason { display: grid; grid-template-columns: 250px 1fr; gap: 4px; padding: 0 3px 4px; }
  .reason + .reason { border-top: 3px solid var(--frame); }
  .reason-head {
    grid-column: 1 / -1; height: 37px; margin: 0 -3px;
    background: var(--teal); color: #fff;
    display: grid; grid-template-columns: 253px 1fr; align-items: center;
    font-weight: 800; font-size: 14px; border-radius: 10px 10px 0 0;
  }
  .reason + .reason .reason-head { border-radius: 10px 10px 0 0; }
  .reason-head span { padding-left: 20px; }
  .reason-head span + span { padding-left: 8px; }
  .prompt, .answer {
    background: var(--paper); border-radius: 8px; height: 82px;
  }
  .prompt {
    display: flex; align-items: center; padding: 0 18px;
    font-size: 11px; line-height: 1.45; color: var(--label);
  }

  .footer-line { position: absolute; left: 0; top: 1171px; width: 848px; height: 7px; background: var(--yellow); }
  .footer-band { position: absolute; left: 0; top: 1180px; width: 848px; height: 20px; background: var(--teal); }
</style>
</head>
<body>
<main class="sheet">
  <div class="backdrop-texture" role="img" aria-label="Soft grey abstract swirl texture in the background"></div>

  <svg class="header-band" viewBox="0 0 600 200" aria-hidden="true">
    <polygon points="0,0 593,0 420,193 0,193" fill="var(--teal)"/>
    <polyline points="596,0 422,196 0,196" fill="none" stroke="var(--yellow)" stroke-width="4"/>
  </svg>
  <div class="brand">VERDAVIA</div>

  <h1 class="doc-title">Health Objectives</h1>

  <div class="field field--nutritionist">Nutritionist’s name:<span class="dots"></span></div>
  <div class="field field--store">Store location:<span class="dots"></span></div>
  <div class="field field--date">Date of consultation:<span class="dots"></span></div>
  <div class="field field--client">Client’s name:<span class="dots"></span></div>

  <section class="objectives">
    <div class="reason">
      <div class="reason-head"><span>Reason 1</span><span>Your comments</span></div>
      <div class="prompt">Symptom, issue or condition you want to address.</div><div class="answer"></div>
      <div class="prompt">Duration - how long have you felt like this or experienced this symptom(s)?</div><div class="answer"></div>
      <div class="prompt">Have you seen a doctor about this for a diagnosis? Did you receive any medical treatment?</div><div class="answer"></div>
      <div class="prompt">Is there any background or extra health or lifestyle information that relates to this situation that you want your practitioner to know about? Please give details.</div><div class="answer"></div>
    </div>
    <div class="reason">
      <div class="reason-head"><span>Reason 2</span><span>Your comments</span></div>
      <div class="prompt">Symptom, issue or condition you want to address.</div><div class="answer"></div>
      <div class="prompt">Duration - how long have you felt like this or experienced this symptom(s)?</div><div class="answer"></div>
      <div class="prompt">Have you seen a doctor about this for a diagnosis? Did you receive any medical treatment?</div><div class="answer"></div>
      <div class="prompt">Is there any background or extra health or lifestyle information that relates to this situation that you want your practitioner to know about? Please give details.</div><div class="answer"></div>
    </div>
  </section>

  <div class="footer-line"></div>
  <div class="footer-band"></div>
</main>
</body>
</html>
```